looking to have a web site for the company which provides services in the industrial and commercial sectors such as: electrical, automation control and system integration, construction and maintenance, millwright, equipment assembly repair and installation. I have the domain already brivanholdings.net and logo. Most recent projects fulfilled for the following clients: MarlowKibbleCo, Dunholt University, OKSU, FALSTO, Tazzik, Prairie Grains

Target Market(s)

industrial and commercial sectors in electrical, automation, millwright and fabrication fields

Industry/Entity Type

Industrial

Coding

Coded - Design and coding required

Number of Pages Required

5+ page

Font styles to use
Sans Serif

Colors

Designer to choose colors to be used in the design.

Requirements
Nice to have
• looking to get something not complicated, nicely presented with minimum or no scrolling

```html
<!DOCTYPE html>
<html lang="en">
<head>
<meta charset="utf-8">
<title>Brivan Holdings</title>
<link href="https://fonts.googleapis.com/css2?family=Raleway:wght@300;400;500;600&family=Open+Sans:wght@400;600&display=swap" rel="stylesheet">
<style>
:root{
  --blue:#0a95e8;
  --blue-dark:#0b6fc4;
  --orange:#e8471c;
  --ink:#1d1d1d;
  --grey-text:#6b6b6b;
  --light:#f3f3f3;
  --footer:#23272c;
  --footer-line:#3a3f46;
  --white:#fff;
}
*{margin:0;padding:0;box-sizing:border-box}
html,body{width:1200px;height:2177px;overflow:hidden;background:var(--white)}
body{position:relative;font-family:'Raleway',sans-serif;color:var(--ink)}
.abs{position:absolute}

/* header */
.top-rule{left:0;top:0;width:1200px;height:4px;background:var(--orange)}
.brand{left:84px;top:30px;width:210px}
.brand-name{font:600 34px/1 'Raleway',sans-serif;color:var(--blue);letter-spacing:1px}
.brand-sub{font:500 14px/1 'Raleway',sans-serif;color:#555;letter-spacing:11px;margin-top:6px}
.contact-bar{right:86px;top:18px;display:flex;align-items:center;gap:8px;font:400 13px 'Open Sans',sans-serif;color:#333}
.contact-bar .sep{color:#bbb;margin:0 8px}
.dot{width:17px;height:17px;border-radius:50%;background:var(--blue);display:inline-block}
.bar-rule{left:632px;top:47px;width:482px;height:1px;background:#e2e2e2}
.nav{right:86px;top:62px;display:flex;font:500 14px 'Raleway',sans-serif}
.nav a{color:var(--ink);text-decoration:none;padding:0 0 0 0}
.nav .pipe{color:#aaa;margin:0 40px}

/* hero */
.hero{left:0;top:91px;width:1200px;height:569px;background:linear-gradient(100deg,#8e9296 0%,#b9bcbf 25%,#7d8185 45%,#a9adb0 62%,#6f7478 78%,#8c9a7a 100%)}
.hero-shade{left:0;top:91px;width:1200px;height:569px;background:linear-gradient(90deg,rgba(20,24,28,.35),rgba(20,24,28,.1) 60%,rgba(20,24,28,.25))}
.hero-title{left:84px;top:300px;font:300 40px/57px 'Raleway',sans-serif;color:var(--white);text-transform:uppercase}
.hero-rule{left:86px;top:416px;width:52px;height:3px;background:var(--blue)}
.hero-text{left:84px;top:432px;width:480px;font:400 18px/28px 'Raleway',sans-serif;color:var(--white)}
.btn-learn{left:87px;top:508px;width:147px;height:46px;border-radius:23px;background:var(--blue);color:var(--white);font:400 18px/46px 'Raleway',sans-serif;text-align:center}

.quote{left:766px;top:184px;width:347px;height:396px;background:rgba(25,25,25,.82)}
.quote-head{left:766px;top:184px;width:347px;height:53px;background:var(--blue);color:var(--white);font:500 22px/53px 'Raleway',sans-serif;text-align:center}
.field{left:800px;width:282px;height:38px;border:1px solid #ddd;color:#bbb;font:400 12px/36px 'Open Sans',sans-serif;padding-left:14px}
.field.msg{height:71px}
.btn-quote{left:800px;top:511px;width:282px;height:38px;background:var(--orange);color:var(--white);font:500 15px/38px 'Raleway',sans-serif;text-align:center}

/* services */
.section-title{left:0;width:1200px;top:728px;text-align:center;font:500 35px/1.2 'Raleway',sans-serif}
.title-line{top:749px;height:1px;background:#c9c9c9;width:100px}
.title-accent{top:748px;height:4px;background:var(--blue-dark);width:30px}
.service{top:823px;width:210px;text-align:center}
.service .circle{width:128px;height:128px;border-radius:50%;background:var(--blue);margin:0 auto;display:flex;align-items:center;justify-content:center}
.service h3{font:400 19px/28px 'Raleway',sans-serif;margin-top:36px;height:56px;text-transform:uppercase}
.service .more{display:inline-block;margin-top:28px;width:102px;height:38px;border:1px solid #999;color:var(--orange);font:500 11px/36px 'Open Sans',sans-serif}
.col-rule{top:868px;width:1px;height:165px;background:#e5e5e5}

/* about */
.about{left:0;top:1187px;width:1200px;height:464px;background:var(--light)}
.about-photo{left:84px;top:1236px;width:498px;height:364px;background:linear-gradient(120deg,#c9d3dc 0%,#9aa6b0 40%,#3c4148 70%,#d6602c 100%)}
.about-title{left:607px;top:1240px;font:500 38px/1.2 'Raleway',sans-serif}
.about-sub{left:608px;top:1297px;font:400 23px/1.2 'Raleway',sans-serif;color:#555}
.about-line{left:657px;top:1345px;width:70px;height:1px;background:#999}
.about-accent{left:680px;top:1344px;width:24px;height:3px;background:var(--blue-dark)}
.about-text{left:607px;top:1366px;width:506px;font:400 14px/22px 'Open Sans',sans-serif;color:var(--grey-text);text-align:justify}
.btn-contact{left:607px;top:1555px;width:139px;height:46px;background:var(--orange);color:var(--white);font:500 14px/46px 'Raleway',sans-serif;text-align:center}

/* clients */
.clients{left:0;top:1680px;width:1200px;height:103px;background:var(--blue-dark)}
.client{top:1716px;height:32px;font:600 17px/32px 'Raleway',sans-serif;color:var(--white);display:flex;align-items:center;gap:8px}
.client .mark{width:14px;height:14px;background:var(--white);border-radius:50%}

/* footer */
.footer{left:0;top:1783px;width:1200px;height:394px;background:var(--footer)}
.f-brand{left:145px;top:1857px}
.f-brand .brand-name{font-size:30px}
.f-brand .brand-sub{font-size:12px;letter-spacing:10px;color:#999}
.f-about{left:145px;top:1920px;width:260px;font:400 13px/22px 'Open Sans',sans-serif;color:#b8bcc2}
.f-contact{left:150px;font:600 13px/1 'Open Sans',sans-serif;color:var(--white);display:flex;align-items:center;gap:12px}
.f-divider{top:1875px;width:1px;height:200px;background:var(--footer-line)}
.f-head{font:400 13px/1 'Open Sans',sans-serif;color:var(--white);text-transform:uppercase}
.f-head-line{width:55px;height:1px;background:var(--blue)}
.post{left:503px;width:220px;color:var(--white)}
.post h4{font:400 14px/1.3 'Open Sans',sans-serif}
.post time{display:block;font:400 10px/1 'Open Sans',sans-serif;color:#aab;margin:10px 0 10px}
.post p{font:400 11px/15px 'Open Sans',sans-serif}
.news-input{left:852px;top:1901px;width:146px;height:38px;border:1px solid #777;color:#999;font:400 11px/36px 'Open Sans',sans-serif;padding-left:14px}
.news-go{left:1006px;top:1901px;width:55px;height:38px;background:var(--orange);color:var(--white);font:600 16px/38px 'Raleway',sans-serif;text-align:center}
.social{left:858px;top:2023px;display:flex;gap:30px}
.social span{width:22px;height:22px;border-radius:50%;background:var(--white)}
.f-bottom-rule{left:0;top:2126px;width:1200px;height:1px;background:var(--footer-line)}
.copyright{left:0;top:2143px;width:1200px;text-align:center;font:400 11px/1 'Open Sans',sans-serif;color:#b8bcc2}
</style>
</head>
<body>

<header>
  <div class="abs top-rule"></div>
  <div class="abs brand">
    <div class="brand-name">BRIVAN</div>
    <div class="brand-sub">HOLDINGS</div>
  </div>
  <div class="abs contact-bar">
    <svg width="17" height="17" viewBox="0 0 17 17"><circle cx="8.5" cy="8.5" r="8.5" fill="#0a95e8"/><path d="M6 4.5h2l.6 2-1.2.8a5 5 0 0 0 2.3 2.3l.8-1.2 2 .6v2c0 .5-.4.8-.9.8A7 7 0 0 1 5.2 5.4c0-.5.3-.9.8-.9z" fill="#fff"/></svg>
    <span>(555) 014-2290</span>
    <span class="sep">|</span>
    <span class="dot"></span><span class="dot"></span>
    <svg width="17" height="17" viewBox="0 0 17 17"><circle cx="8.5" cy="8.5" r="8.5" fill="#0a95e8"/><circle cx="7.6" cy="7.6" r="3" fill="none" stroke="#fff" stroke-width="1.5"/><path d="M9.8 9.8l2.6 2.6" stroke="#fff" stroke-width="1.6"/></svg>
  </div>
  <div class="abs bar-rule"></div>
  <nav class="abs nav">
    <a href="#">HOME</a><span class="pipe">|</span>
    <a href="#">ABOUT US</a><span class="pipe">|</span>
    <a href="#">SERVICES</a><span class="pipe">|</span>
    <a href="#">BLOG</a><span class="pipe">|</span>
    <a href="#">CONTACT US</a>
  </nav>
</header>

<section class="hero-block">
  <div class="abs hero" role="img" aria-label="Industrial grain silos and processing plant under a cloudy sky"></div>
  <div class="abs hero-shade"></div>
  <h1 class="abs hero-title">Lorem Ipsum<br>is simply dummy</h1>
  <div class="abs hero-rule"></div>
  <p class="abs hero-text">text of the printing and typesetting industry. Lorem Ipsum has been the industry's</p>
  <div class="abs btn-learn">Learn More</div>

  <div class="abs quote"></div>
  <div class="abs quote-head">REQUEST SERVICE</div>
  <div class="abs field" style="top:266px">Name..</div>
  <div class="abs field" style="top:319px">Email..</div>
  <div class="abs field" style="top:373px">Phone..</div>
  <div class="abs field msg" style="top:425px">Massege..</div>
  <div class="abs btn-quote">GET A QUOTE</div>
</section>

<section class="services">
  <div class="abs title-line" style="left:324px"></div>
  <div class="abs title-accent" style="left:422px"></div>
  <h2 class="abs section-title">OUR SERVICES</h2>
  <div class="abs title-accent" style="left:748px"></div>
  <div class="abs title-line" style="left:776px"></div>

  <div class="abs service" style="left:72px">
    <div class="circle"><svg width="56" height="64" viewBox="0 0 56 64" fill="none" stroke="#fff" stroke-width="3"><path d="M18 4v14M38 4v14M10 18h36v14a18 18 0 0 1-36 0z"/><path d="M28 50v12"/><path d="M30 24l-5 10h6l-5 10" stroke-width="2.5"/></svg></div>
    <h3>Electrical</h3><span class="more">READ MORE</span>
  </div>
  <div class="abs col-rule" style="left:277px"></div>
  <div class="abs service" style="left:282px">
    <div class="circle"><svg width="64" height="64" viewBox="0 0 64 64" fill="none" stroke="#fff" stroke-width="3"><circle cx="24" cy="24" r="9"/><circle cx="24" cy="24" r="16" stroke-dasharray="6 4"/><circle cx="46" cy="46" r="6"/><circle cx="46" cy="46" r="11" stroke-dasharray="4 3"/></svg></div>
    <h3>Automation<br>Control...</h3><span class="more">READ MORE</span>
  </div>
  <div class="abs col-rule" style="left:490px"></div>
  <div class="abs service" style="left:494px">
    <div class="circle"><svg width="64" height="56" viewBox="0 0 64 56" fill="none" stroke="#fff" stroke-width="3"><rect x="6" y="6" width="52" height="44"/><path d="M20 30l12-10 12 10M24 28v14h16V28"/><rect x="29" y="34" width="6" height="8"/></svg></div>
    <h3>Construction...</h3><span class="more">READ MORE</span>
  </div>
  <div class="abs col-rule" style="left:702px"></div>
  <div class="abs service" style="left:703px">
    <div class="circle"><svg width="60" height="60" viewBox="0 0 60 60" fill="none" stroke="#fff" stroke-width="3"><path d="M8 52L40 20M36 8a10 10 0 0 0 14 14l-6-6z"/><path d="M52 52L20 20M10 10l8-2 6 6-2 8-8-6z"/></svg></div>
    <h3>Millwright</h3><span class="more">READ MORE</span>
  </div>
  <div class="abs col-rule" style="left:913px"></div>
  <div class="abs service" style="left:915px">
    <div class="circle"><svg width="60" height="60" viewBox="0 0 60 60" fill="none" stroke="#fff" stroke-width="3"><circle cx="30" cy="30" r="10"/><circle cx="30" cy="30" r="20" stroke-dasharray="7 5"/></svg></div>
    <h3>Equipment<br>Assembly...</h3><span class="more">READ MORE</span>
  </div>
</section>

<section class="about-block">
  <div class="abs about"></div>
  <div class="abs about-photo" role="img" aria-label="Mechanic in safety glasses inspecting a car engine while a colleague takes notes on a clipboard"></div>
  <h2 class="abs about-title">ABOUT US</h2>
  <div class="abs about-sub">BRIVAN HOLDINGS LTD.</div>
  <div class="abs about-line"></div>
  <div class="abs about-accent"></div>
  <p class="abs about-text">Lorem Ipsum is simply dummy text of the printing and typesetting industry. Lorem Ipsum has been the industry's standard dummy text ever since the 1500s, when an unknown printer took a galley of type and scrambled it to make a type specimen book. It has survived not only five centuries, but also the leap into electronic typesetting, remaining essentially unchanged. It was popularised in the 1960s with the release of Letraset sheets containing Lorem Ipsum passages</p>
  <div class="abs btn-contact">CONTACT US</div>
</section>

<section class="client-band">
  <div class="abs clients"></div>
  <div class="abs client" style="left:86px"><span class="mark"></span>MarlowKibbleCo</div>
  <div class="abs client" style="left:290px">Dunholt University</div>
  <div class="abs client" style="left:470px"><span class="mark"></span>OKSU</div>
  <div class="abs client" style="left:630px"><span class="mark"></span>FALSTO</div>
  <div class="abs client" style="left:812px">Tazzik</div>
  <div class="abs client" style="left:980px">Prairie Grains</div>
</section>

<footer>
  <div class="abs footer"></div>
  <div class="abs f-brand"><div class="brand-name">BRIVAN</div><div class="brand-sub">HOLDINGS</div></div>
  <p class="abs f-about">Lorem Ipsum is simply dummy text of the printing and typesetting industry.</p>
  <div class="abs f-contact" style="top:2009px">
    <svg width="13" height="13" viewBox="0 0 13 13"><path d="M2 1h3l1 3-1.6 1a6 6 0 0 0 3.6 3.6L9 7l3 1v3c0 .6-.4 1-1 1A10 10 0 0 1 1 2c0-.6.4-1 1-1z" fill="#0a95e8"/></svg>(555) 016-3381</div>
  <div class="abs f-contact" style="top:2040px;font-weight:400">
    <svg width="14" height="11" viewBox="0 0 14 11"><rect x="0.5" y="0.5" width="13" height="10" fill="#0a95e8"/><path d="M1 1l6 5 6-5" stroke="#fff" fill="none"/></svg>info@brivanholdings.net</div>

  <div class="abs f-divider" style="left:425px"></div>
  <div class="abs f-head" style="left:505px;top:1855px">RECENT BLOG POSTS</div>
  <div class="abs f-head-line" style="left:505px;top:1877px"></div>
  <article class="abs post" style="top:1895px">
    <h4>Nulla consequat massa quis enim</h4><time>November 19, 2016</time>
    <p>The sight of the tumblers restored Bob Sawyer ...</p>
  </article>
  <article class="abs post" style="top:2015px">
    <h4>Nulla consequat massa quis enim</h4><time>November 19, 2016</time>
    <p>The sight of the tumblers restored Bob Sawyer to ...</p>
  </article>

  <div class="abs f-divider" style="left:795px"></div>
  <div class="abs f-head" style="left:852px;top:1855px">NEWSLETTER</div>
  <div class="abs f-head-line" style="left:852px;top:1877px"></div>
  <div class="abs news-input">Your Email Id....</div>
  <div class="abs news-go">GO</div>
  <div class="abs f-head" style="left:852px;top:1978px">FOLLOW US</div>
  <div class="abs f-head-line" style="left:852px;top:2000px"></div>
  <div class="abs social"><span></span><span></span><span></span><span></span></div>

  <div class="abs f-bottom-rule"></div>
  <div class="abs copyright">brivanholdings.net 2017. All rights reserved</div>
</footer>

</body>
</html>
```